TILLvanta (www.tillvanta.example) needs exciting professional Business Cards

TILLvanta is an exciting new start-up targeting innovative ways to engage with retail customers at the point of sale.
Our Vision
Through applying new thinking to an old business we are reinventing selected segments of the Australian retail messaging industry, generating significant value for our customers, our suppliers, and our owners.
We operate with integrity, agility, and intelligence to doing things smarter, faster and more efficiently.
We bring deep industry expertise, deep relationships with customers and suppliers, and a will to see the old ways give way to smarter ways – this is why we win.
From this economically sustainable platform, we will examine the disruption of other market segments by further leveraging the elements that make us successful.
Our Values
With our clients, with our suppliers, with our staff, and with our owners:
# We Partner – We align the interest of all stakeholders by striving to ensure everything we do is mutually beneficial and commercially sustainable in the long term. We are clear with all our stakeholders about what our expectations are of them, and we seek clarity from them in their expectations of us.
# We Innovate – In the segments we choose to compete in, we bring fresh ideas, new business processes, the right relationships, and the right technology to ensure the supply chain is nimble, competitive, and reliable.
# We are Accountable – We say what we will do, and then do what we say.
# We Perform – We use our skills, relationships, and reputation to deliver value to our customers, suppliers, and owners.
Initially we are building our business from low-tech through printing promotional offers and retailer messages on ATM and EFTPOS receipts, but as soon as cash flow supports it we will be engaging in high-tech real-time targeted offers to the specific consumer.
I'd like the cards to reflect our values.
Please check out the web site we have just launched - it is pretty basic but it has only been up a week. We intend to sharpen it over the coming weeks, but you'll get the idea of what our core messages are.
I have recently sourced a logo from MarkForge, and have attached the source files for use.
Personal information to include:
Name: FirstName Surname
Title: Managing Director
email: first.surname@tillvanta.example
Mobile: +61-427-318-654
Generic Co Details to include:
Web: www.tillvanta.example
email: tillvanta@tillvanta.example
Fax: +61-8-7394-2816
Offices & Agents: Sydney, Melbourne, Brisbane, Adelaide, Perth
Byline: Innovation . Integrity . Service
Target Market(s)
Our customers are large corporations that have professional Point Of Sale marketing experts looking for a supplier with an edge over others in a crowded market. The buyer of our product and services is ultimately a communications expert.
They want to see distinctive competence, and an agility of thinking that will make them money through driving more consumer spending.
Industry/Entity Type
Retail
Look and feel
Each slider illustrates characteristics of the customer's brand and the style your logo design should communicate.

```html
<!DOCTYPE html>
<html lang="en">
<head>
<meta charset="UTF-8">
<title>TILLvanta Business Cards</title>
<link rel="stylesheet" href="https://fonts.googleapis.com/css2?family=Montserrat:wght@400;600;700&display=swap">
<style>
  :root {
    --backdrop: #3a3a3c;
    --card-light: #e9e7e0;
    --card-dark: #25272b;
    --brand-blue: #1a7fc1;
    --text-light: #e6e6e6;
    --text-muted: #b9b9b9;
    --text-grey: #6f6f6f;
  }
  * { margin: 0; padding: 0; box-sizing: border-box; }
  html, body {
    width: 1200px; height: 900px; overflow: hidden;
    background: var(--backdrop);
    font-family: "Montserrat", sans-serif;
  }
  .canvas { position: relative; width: 1200px; height: 900px; }
  .card {
    position: absolute; left: 280px; width: 640px; height: 360px;
    box-shadow: 0 10px 30px rgba(0,0,0,.35);
  }
  .card--back { top: 60px; background: var(--card-light); }
  .card--front { top: 480px; background: var(--card-dark); }

  .company-name {
    position: absolute;
    color: var(--brand-blue);
    font-weight: 600; font-size: 40px; line-height: 1;
    letter-spacing: 3px; text-transform: uppercase;
  }
  .card--back .company-name { left: 120px; top: 130px; }
  .card--front .company-name { left: 60px; top: 120px; }

  .offices {
    position: absolute; left: 122px; top: 220px;
    font-size: 12px; color: var(--text-grey); line-height: 1.7;
  }
  .offices__label { font-weight: 700; letter-spacing: 1px; text-transform: uppercase; }

  .person { position: absolute; left: 60px; top: 268px; color: var(--text-light); }
  .person__name { font-weight: 700; font-size: 17px; letter-spacing: 1px; text-transform: uppercase; }
  .person__title { font-size: 13px; color: var(--text-muted); margin-top: 3px; }

  .contacts {
    position: absolute; top: 262px; list-style: none;
    font-size: 12px; color: var(--text-muted);
  }
  .contacts--phone { left: 280px; }
  .contacts--web { left: 420px; }
  .contacts li { display: flex; align-items: center; gap: 8px; margin-bottom: 9px; white-space: nowrap; }
  .contacts svg { width: 14px; height: 14px; flex: none; }
</style>
</head>
<body>
<main class="canvas">

  <section class="card card--back" aria-label="Card reverse">
    <p class="company-name">TILLvanta</p>
    <p class="offices">
      <span class="offices__label">Offices &amp; Agents:</span><br>
      Sydney, Melbourne, Brisbane, Adelaide, Perth
    </p>
  </section>

  <section class="card card--front" aria-label="Card front">
    <p class="company-name">TILLvanta</p>

    <div class="person">
      <p class="person__name">Jordan Keller</p>
      <p class="person__title">Managing Director</p>
    </div>

    <ul class="contacts contacts--phone">
      <li>
        <svg viewBox="0 0 14 14"><circle cx="7" cy="7" r="7" fill="#1a7fc1"/><rect x="5" y="3.5" width="4" height="7" rx="0.8" fill="none" stroke="#fff" stroke-width="1"/></svg>
        +61-427-318-654
      </li>
      <li>
        <svg viewBox="0 0 14 14"><circle cx="7" cy="7" r="7" fill="#1a7fc1"/><rect x="4" y="5" width="6" height="5" fill="none" stroke="#fff" stroke-width="1"/><line x1="5" y1="3.5" x2="9" y2="3.5" stroke="#fff" stroke-width="1"/></svg>
        +61-8-7394-2816
      </li>
    </ul>

    <ul class="contacts contacts--web">
      <li>
        <svg viewBox="0 0 14 14"><circle cx="7" cy="7" r="7" fill="#1a7fc1"/><rect x="3.5" y="4.5" width="7" height="5" fill="none" stroke="#fff" stroke-width="1"/><polyline points="3.5,4.5 7,7.5 10.5,4.5" fill="none" stroke="#fff" stroke-width="1"/></svg>
        j.keller@tillvanta.example
      </li>
      <li>
        <svg viewBox="0 0 14 14"><circle cx="7" cy="7" r="7" fill="#1a7fc1"/><circle cx="7" cy="7" r="3.5" fill="none" stroke="#fff" stroke-width="1"/><line x1="3.5" y1="7" x2="10.5" y2="7" stroke="#fff" stroke-width="1"/></svg>
        www.tillvanta.example
      </li>
    </ul>
  </section>

</main>
</body>
</html>
```